Lost & Found Website - PAYMENT GUARANTY

PC website and Mobile Website

Our website aims to develop an online management platform for lost & found objects with the use of stickers.
This solution allows users to buy stickers which will be affixed on the owners’ objects (glasses, laptops, phones …).
Users shall register the code on the website or the mobile application (flashing QR code). Platform will alert by email users if its object is found.
The person who finds an object with a sticker will be encouraged to declare the code on the web/mobile site. Once the object is found, it is identified by the system and the platform notifies the owner via email and give access to contact details of the person who found the object.

PLEASE SEE REQUIREMENT ATTACHED
Updates

Project Deadline Extended
Reason: We are waiting for more interesting ideas. Thank you all for your work. B. Lorimond

Project Deadline Extended
Reason: Your designs are very next to perfection !

Target Market(s)

Our target are people 20 to 35 years old who care about there objects. Mainly French market at the beginning.

Industry/Entity Type

Management

Requirements
Must have
• Specifications:

The design must follow basic web design rules:
- Consistent site header/logo
- Page footer area includes copyright, last update, contact e-mail address
- Color scheme is limited to a maximum of three or four colors plus neutrals
- Color is used consistently
- Common fonts such as Arial or Times New Roman are used
- No more than one web font is used
- Fonts, font sizes, and font colors are consistently used
- Information is easy to find (minimal clicks)
- Find a suitable place to put the sponsor's logos.

For mobile version, we need a design that can fit to any screen size,
so please create standard mobile design.
Nice to have
• The website should allow users to:
- Create an account
- Buy lots of stickers
- Associate stickers to their objects
- Report the loss of an object by email
- Access full contact information of the finder after he paid the service
- Declare a found object
- The payment process management via Quidora platform
Should not have
• Only PSD files.

No html.

```html
<!DOCTYPE html>
<html lang="en">
<head>
<meta charset="utf-8">
<title>Trouvio – Online Lost &amp; Found</title>
<link href="https://fonts.googleapis.com/css2?family=Tinos:ital,wght@0,400;0,700;1,400&family=Noto+Sans:wght@400;700&family=Arvo:wght@700&display=swap" rel="stylesheet">
<style>
:root{
  --red:#e60000;
  --blue:#3a7db8;
  --sky:#5fa8d3;
  --steel:#6e90ae;
  --ink:#222;
  --paper:#ececec;
  --navy:#1d3550;
  --white:#fff;
}
*{margin:0;padding:0;box-sizing:border-box}
html,body{width:985px;height:1200px;overflow:hidden}
body{position:relative;background:var(--paper);font-family:"Noto Sans",sans-serif;color:var(--ink);border-top:3px solid var(--red)}
a{color:inherit;text-decoration:none}
.abs{position:absolute}

.brand{left:10px;top:27px;width:200px;height:86px;background:var(--white);border:1px solid #bbb;border-radius:12px;box-shadow:2px 3px 5px rgba(0,0,0,.25);display:flex;align-items:center;justify-content:center;gap:8px;font-family:"Tinos",serif;font-size:32px;color:#111}
.brand-dot{width:12px;height:12px;border-radius:50%;background:#111}

.cta-btn{top:24px;width:140px;height:50px;border-radius:7px;border:2px solid #aab;background:linear-gradient(#4d6a86,#223a52);color:var(--white);font-family:"Arvo",serif;font-size:14px;line-height:17px;text-align:center;display:flex;align-items:center;justify-content:center}
.cta-register{left:408px}
.cta-found{left:556px}

.account-links{left:722px;top:44px;font-size:13px}
.account-links span{margin:0 7px}
.cart{left:941px;top:35px;width:34px;height:34px;border-radius:7px;background:var(--red);display:flex;align-items:center;justify-content:center}
.cart b{position:absolute;top:-1px;left:11px;font-size:9px;color:var(--white)}

.main-nav{left:313px;top:94px;display:flex;gap:20px;font-size:14px;align-items:center}
.main-nav a{text-decoration:underline;padding:4px 0}
.main-nav .current{background:var(--sky);padding:4px 12px;border-radius:3px}
.lang{left:872px;top:98px;background:var(--sky);color:var(--white);font-size:12px;padding:1px 7px}

.hero{left:11px;top:142px;width:964px;height:339px;border-radius:8px;background:radial-gradient(ellipse at 60% 35%,#6f8ea8,#3a566f 60%,#24384c);overflow:hidden}
.hero-copy{left:30px;top:32px;color:var(--white);font-family:"Tinos",serif}
.hero-copy .welcome{font-style:italic;font-size:21px}
.hero-copy .line{font-size:45px;line-height:48px}
.hero-copy .big{font-size:58px;line-height:58px;font-weight:700}
.hero-copy .lost{color:var(--red)}
.hero-copy .dept{font-size:45px}
.hero-text{left:30px;top:233px;width:450px;color:var(--white);font-size:14px;line-height:24px}

.signup{left:534px;top:36px;width:406px;height:240px;background:rgba(200,212,222,.55);border-radius:10px}
.signup-badge{left:26px;top:0;width:62px;height:46px;background:var(--white);border-radius:0 0 8px 8px;display:flex;align-items:center;justify-content:center}
.signup-badge i{width:20px;height:20px;border-radius:50%;border:2px solid #333}
.signup-title{left:96px;top:8px;font-family:"Arvo",serif;font-weight:700;font-size:14px;line-height:20px;color:#243340;width:300px}
.field{left:26px;width:356px;height:48px;background:#e8eef2;border-radius:9px;padding:14px 11px;font-size:13px;font-weight:700;color:#222}
.field-email{top:55px}.field-pass{top:118px}
.btn-signup{left:27px;top:181px;width:166px;height:30px;background:#222;color:var(--white);font-weight:700;font-size:14px;text-align:center;line-height:30px}
.btn-social{left:219px;top:181px;width:164px;height:30px;background:#3b5a97;color:var(--white);font-size:13px;text-align:center;line-height:30px}
.signup-links{left:29px;top:219px;font-size:12px;color:#111}

.applies{left:28px;top:301px;width:918px;height:30px;background:rgba(30,50,80,.75);border-radius:3px;display:flex;align-items:center;gap:22px;padding-left:9px}
.applies span{color:#7ecbf0;font-size:12px;margin-right:20px}
.applies svg{flex:none}

.step{top:497px;width:313px;height:283px;border:3px solid var(--steel);border-radius:6px;background:#dcdde0;overflow:hidden}
.step-1{left:10px}.step-2{left:336px}.step-3{left:662px}
.step-art{left:0;top:0;width:100%;height:222px}
.art-1{background:linear-gradient(#f6f6f6,#d7d7d7)}
.art-2{background:linear-gradient(#f4f4f4,#c9ccd0)}
.art-3{background:linear-gradient(#f8f8f8,#d5d6d8)}
.step-num{left:0;top:236px;width:32px;height:32px;background:#222;color:var(--white);font-weight:700;font-size:13px;clip-path:polygon(0 0,65% 0,100% 50%,65% 100%,0 100%);padding:8px 0 0 8px}
.step-text{left:47px;top:235px;font-size:13px;line-height:16px}
.step-text h3{color:var(--blue);font-size:14px}
.step-text strong{font-size:12px;letter-spacing:.4px}

.about{left:11px;top:800px;width:635px}
.about h2,.sponsors h2{font-size:18px;letter-spacing:1px;font-weight:700}
.about p{font-size:14px;line-height:25px;margin-top:4px}
.about a{font-size:12px;font-weight:700;text-decoration:underline;color:#2e4457}

.ad{left:662px;width:313px;height:114px;background:var(--steel);display:flex;align-items:center;justify-content:center;font-size:14px;color:#222;border-radius:2px}
.ad-1{top:800px}.ad-2{top:929px}

.sponsors{left:11px;top:927px;width:635px}
.sponsor-row{margin-top:12px;border-top:1px dashed #8aa;border-bottom:1px dashed #8aa;height:84px;display:flex;align-items:center;justify-content:space-between}
.sponsor-row span{font-size:20px;font-weight:700;color:#3a4d6a}
.sponsor-row .boxed{background:#c9c9c9;padding:8px 14px;color:#111}

.footer{left:0;top:1083px;width:985px;height:117px;background:var(--red)}
.quick{top:18px;width:280px;height:48px;background:linear-gradient(#fff,#dadada);border-radius:8px;display:flex;overflow:hidden;font-size:14px}
.quick span{flex:1;padding:15px 14px}
.quick b{width:41px;background:#222;color:var(--white);font-weight:400;font-size:13px;display:flex;align-items:center;justify-content:center}
.quick-register{left:205px}.quick-found{left:500px}
.footer-links{left:168px;top:82px;display:flex;align-items:center;color:var(--white);font-size:12px;gap:10px}
.footer-links .name{font-size:18px;font-weight:700;margin-right:12px}
.footer-links .pay{font-weight:700;font-size:14px}
.social{display:flex;gap:10px;margin-left:14px}
.social i{width:20px;height:20px;border-radius:4px;background:#4c87c5;display:block}
</style>
</head>
<body>

<header>
  <a class="abs brand" href="#"><span class="brand-dot"></span>Trouvio</a>
  <a class="abs cta-btn cta-register" href="#">Register<br>Trouvio Code</a>
  <a class="abs cta-btn cta-found" href="#">I found<br>an object!</a>
  <nav class="abs account-links"><a href="#">Login</a><span>|</span><a href="#">Register</a><span>|</span><a href="#">My Account</a></nav>
  <a class="abs cart" href="#"><b>4</b>
    <svg width="20" height="18" viewBox="0 0 20 18"><path d="M1 2h3l3 9h9l2-6H6" fill="none" stroke="#fff" stroke-width="2"/><circle cx="8" cy="15" r="1.8" fill="#fff"/><circle cx="15" cy="15" r="1.8" fill="#fff"/></svg>
  </a>
  <nav class="abs main-nav">
    <a class="current" href="#">Home</a><a href="#">About Us</a><a href="#">How Does It Work</a><a href="#">Buy Stickers</a><a href="#">Q&amp;A</a><a href="#">Contact</a>
  </nav>
  <div class="abs lang">English / French</div>
</header>

<section class="abs hero" role="img" aria-label="Faded world map on a steel blue background">
  <div class="abs hero-copy">
    <div class="welcome">WELCOME,</div>
    <div class="line">WE ARE ONLINE</div>
    <div class="big"><span class="lost">LOST</span> &amp; <span class="lost">FOUND</span></div>
    <div class="dept">DEPARTMENT</div>
  </div>
  <p class="abs hero-text"><b>Trouvio</b> is next generation lost &amp; found service for Web and Mobile for people and businesses all around the world.</p>

  <form class="abs signup">
    <div class="abs signup-badge"><i></i></div>
    <p class="abs signup-title">Sign up below and make your stuff come back to you!</p>
    <div class="abs field field-email">Your email</div>
    <div class="abs field field-pass">Password</div>
    <div class="abs btn-signup">Sign me up</div>
    <div class="abs btn-social">Login With Chatterly</div>
    <p class="abs signup-links">Create an account | Trouble logging in?</p>
  </form>

  <div class="abs applies">
    <span>Trouvio Stickers can be applied on</span>
    <svg width="18" height="14" viewBox="0 0 18 14"><path d="M8 1 2 7l6 6M16 1l-6 6 6 6" fill="none" stroke="#5fa8d3" stroke-width="2.5"/></svg>
    <svg width="30" height="22" viewBox="0 0 30 22"><rect x="1" y="5" width="28" height="16" rx="2" fill="#5fa8d3"/><rect x="9" y="1" width="10" height="5" fill="#5fa8d3"/><circle cx="15" cy="13" r="5" fill="#1d3550"/></svg>
    <svg width="16" height="26" viewBox="0 0 16 26"><rect x="1" y="1" width="14" height="24" rx="3" fill="none" stroke="#5fa8d3" stroke-width="2"/></svg>
    <svg width="36" height="18" viewBox="0 0 36 18"><rect x="1" y="4" width="34" height="10" rx="5" fill="#5fa8d3"/><circle cx="12" cy="9" r="7" fill="#1d3550" stroke="#5fa8d3" stroke-width="2"/></svg>
    <svg width="44" height="16" viewBox="0 0 44 16"><circle cx="11" cy="8" r="7" fill="none" stroke="#5fa8d3" stroke-width="2.5"/><circle cx="33" cy="8" r="7" fill="none" stroke="#5fa8d3" stroke-width="2.5"/><path d="M18 7h8" stroke="#5fa8d3" stroke-width="2.5"/></svg>
    <svg width="32" height="22" viewBox="0 0 32 22"><rect x="5" y="1" width="22" height="15" fill="none" stroke="#5fa8d3" stroke-width="2"/><rect x="1" y="17" width="30" height="3" fill="#5fa8d3"/></svg>
    <svg width="24" height="26" viewBox="0 0 24 26"><path d="M7 9a5 5 0 0 1 10 0" fill="none" stroke="#5fa8d3" stroke-width="2"/><rect x="2" y="9" width="20" height="16" rx="6" fill="#5fa8d3"/></svg>
    <svg width="36" height="20" viewBox="0 0 36 20"><rect x="1" y="3" width="24" height="15" fill="#5fa8d3"/><path d="M26 10l9-6v12z" fill="#5fa8d3"/></svg>
    <svg width="40" height="16" viewBox="0 0 40 16"><circle cx="8" cy="8" r="7" fill="#5fa8d3"/><path d="M14 8h24M32 8v6M37 8v5" stroke="#5fa8d3" stroke-width="3"/></svg>
    <svg width="30" height="26" viewBox="0 0 30 26"><path d="M4 18V13a11 11 0 0 1 22 0v5" fill="none" stroke="#5fa8d3" stroke-width="2.5"/><rect x="2" y="16" width="6" height="9" rx="2" fill="#5fa8d3"/><rect x="22" y="16" width="6" height="9" rx="2" fill="#5fa8d3"/></svg>
    <svg width="26" height="20" viewBox="0 0 26 20"><rect x="1" y="2" width="24" height="17" rx="2" fill="#5fa8d3"/><rect x="16" y="8" width="9" height="6" fill="#1d3550"/></svg>
    <svg width="18" height="14" viewBox="0 0 18 14"><path d="M2 1l6 6-6 6M10 1l6 6-6 6" fill="none" stroke="#5fa8d3" stroke-width="2.5"/></svg>
  </div>
</section>

<section>
  <article class="abs step step-1">
    <div class="abs step-art art-1" role="img" aria-label="Figure lying in front of a laptop with sticker rolls"></div>
    <div class="abs step-num">1</div>
    <div class="abs step-text"><h3>Buy Sticker</h3>Register trovel code &nbsp;| &nbsp;<strong>BUY STICKERS</strong></div>
  </article>
  <article class="abs step step-2">
    <div class="abs step-art art-2" role="img" aria-label="Phone, laptop and wallet with sticker rolls applied"></div>
    <div class="abs step-num">2</div>
    <div class="abs step-text"><h3>Paste Sticker</h3>Put it on your device</div>
  </article>
  <article class="abs step step-3">
    <div class="abs step-art art-3" role="img" aria-label="Figures celebrating beside a laptop, phone and email sign"></div>
    <div class="abs step-num">3</div>
    <div class="abs step-text"><h3>Get Email Alerts</h3>When item is found</div>
  </article>
</section>

<section class="abs about">
  <h2>TROUVIO</h2>
  <p>Loraim lipsum there idfd vhgh lid dtiday dfdf0dfadidf&nbsp; Lidf idfhis uil uigioi. Loraim lipsum there idfd vhgh lid dtiday dfdf0dfadidf&nbsp; Lidf idfhis uil uigioi.Loraim lipsum there idfd vhgh lid dtiday dfdf0dfadidf&nbsp; Lidf idfhis uil uigioi. <a href="#">LEARN MORE</a></p>
</section>

<section class="abs sponsors">
  <h2>OUR &nbsp;SPONSORS</h2>
  <div class="sponsor-row">
    <span>Norvik</span><span>Selmara</span><span>Parcelo</span><span>Fizzora</span><span class="boxed">Bolt Ten</span>
  </div>
</section>

<aside>
  <div class="abs ad ad-1">Ads Goes Here!</div>
  <div class="abs ad ad-2">Ads Goes Here!</div>
</aside>

<footer class="abs footer">
  <div class="abs quick quick-register"><span>Register Trouvio code</span><b>GO</b></div>
  <div class="abs quick quick-found"><span>Found Trovel Code?</span><b>GO</b></div>
  <nav class="abs footer-links">
    <span class="name">Trouvio</span>
    <a href="#">Privacy</a>|<a href="#">Terms of Use</a>|<a href="#">Buy Stickers</a>|<a href="#">Contact</a>|<span class="pay">Quidora</span>
    <span class="social"><i></i><i></i><i></i><i></i></span>
  </nav>
</footer>

</body>
</html>
```